Advertising material for new program

We are launching a new program and need some advertising material.
- Cover photo for facebook (with minimal words on it)
- Social Media graphic (with minimal words on it)
- a5 flyer
- Banner

Information:
- Sensory play is a NEW program at Ember Tumblehall
What is Sensory Play:
*A sensory experience for babies 0 - 13months old.
* Stimulating babies senses
* Engaging movement and balance
- Created by qualified early childhood professional
- starting on Wednesdays in February 2022
- Book online
*www.embertumblehall.example
-Contact us for more information
*97316258
*info@embertumblehall.example

NOT INFORMATION FOR THE ADVERTISING
I have attached our style guide, our logo, some material we have done done recently and some photo of my own baby. As its a new program we don't have any photos yet but I am open to ideas

Target Market(s)

Mums aged 25 - 45

Industry/Entity Type

Kids activities

Colors
0054AA
0677BA
7BADD7
CADEEF
E8F1F8
59FF00
82FF00
B8FF75
E3FFCB
F4FFEA

Requirements
Must have
• photos of babies and mums with babies
Should not have
• Photos of adults / teens

```html
<!DOCTYPE html>
<html lang="en">
<head>
<meta charset="utf-8">
<title>Sensory Play – Ember Tumblehall</title>
<link rel="stylesheet" href="https://fonts.googleapis.com/css2?family=Exo+2:ital,wght@1,900&family=Black+Ops+One&family=Montserrat:wght@700;800&family=Oswald:wght@700&display=swap">
<style>
  :root {
    --lime: #a3cc14;
    --lime-bright: #b5e01c;
    --lime-pale: #d9ef9a;
    --navy: #17284a;
    --navy-deep: #0f1c36;
    --forest: #2f5a14;
    --paper: #ffffff;
    --mist: #eceeef;
    --fog: #d7dadc;
    --photo-warm: #e9e3dc;
    --photo-green: #7fc43a;
  }
  * { box-sizing: border-box; margin: 0; padding: 0; }
  html, body { width: 1200px; height: 457px; overflow: hidden; background: var(--paper); }
  .cover {
    position: relative;
    width: 1200px;
    height: 457px;
    overflow: hidden;
    isolation: isolate;
    background: linear-gradient(90deg, var(--paper) 40%, var(--mist) 100%);
    font-family: "Montserrat", sans-serif;
  }
  .art { position: absolute; inset: 0; z-index: 0; }
  .brand {
    position: absolute;
    z-index: 2;
    display: flex;
    align-items: center;
    gap: 8px;
    color: var(--navy);
    font-family: "Montserrat", sans-serif;
    font-weight: 800;
    white-space: nowrap;
  }
  .brand-dot { border-radius: 50%; background: var(--lime); flex: none; }
  .brand--main { left: 926px; top: 62px; font-size: 23px; }
  .brand--main .brand-dot { width: 22px; height: 22px; }
  .brand--small { left: 278px; top: 341px; font-size: 12px; gap: 5px; }
  .brand--small .brand-dot { width: 12px; height: 12px; }

  .kicker {
    position: absolute;
    z-index: 2;
    left: 490px; top: 84px;
    width: 360px;
    text-align: center;
    font-family: "Exo 2", sans-serif;
    font-style: italic;
    font-weight: 900;
    font-size: 46px;
    letter-spacing: -1px;
    color: var(--lime-bright);
    -webkit-text-stroke: 1px var(--forest);
  }
  .headline { position: absolute; z-index: 2; left: 430px; top: 148px; width: 740px; height: 100px; }

  .audience {
    position: absolute;
    z-index: 2;
    left: 526px; top: 265px;
    width: 452px; height: 38px;
    display: flex; align-items: center; justify-content: center;
    color: var(--paper);
    font-weight: 800;
    font-size: 21px;
    letter-spacing: 0.2px;
    background: var(--navy);
    clip-path: polygon(2% 0, 100% 0, 98% 100%, 0 100%);
    box-shadow: inset 0 -2px 0 var(--lime);
  }

  .schedule { position: absolute; z-index: 2; left: 628px; top: 314px; display: flex; align-items: stretch; }
  .schedule-day { display: flex; flex-direction: column; align-items: center; }
  .schedule-label { color: var(--navy); font-weight: 800; font-size: 19px; line-height: 22px; margin-top: 17px; }
  .schedule-weekday {
    background: var(--navy); color: var(--paper);
    font-weight: 700; font-size: 19px; line-height: 23px;
    padding: 0 6px; margin-top: 3px;
  }
  .schedule-divider { width: 3px; background: var(--lime); margin: 24px 6px 0; }
  .schedule-month { display: flex; flex-direction: column; align-items: flex-start; font-family: "Oswald", sans-serif; font-weight: 700; color: var(--navy); }
  .schedule-year { font-size: 50px; line-height: 46px; letter-spacing: 1px; }
  .schedule-name { font-size: 25px; line-height: 26px; letter-spacing: 0.5px; }

  .contact-item {
    position: absolute; z-index: 2; top: 414px;
    display: flex; align-items: center; gap: 8px;
    color: var(--navy); font-weight: 800; font-size: 13px; white-space: nowrap;
  }
  .contact-item svg { flex: none; }
  .contact-item--phone { left: 402px; }
  .contact-item--mail { left: 565px; }
  .contact-item--web { left: 884px; }
</style>
</head>
<body>
<div class="cover">
  <svg class="art" width="1200" height="457" viewBox="0 0 1200 457">
    <defs>
      <linearGradient id="photoTone" x1="0" y1="0" x2="0.6" y2="1">
        <stop offset="0" stop-color="#f1ede8"/>
        <stop offset="0.45" stop-color="#e9e3dc"/>
        <stop offset="0.75" stop-color="#cfe3b5"/>
        <stop offset="1" stop-color="#7fc43a"/>
      </linearGradient>
      <linearGradient id="hazeTone" x1="0" y1="0" x2="1" y2="0">
        <stop offset="0" stop-color="#ffffff" stop-opacity="0"/>
        <stop offset="1" stop-color="#d7dadc"/>
      </linearGradient>
    </defs>

    <rect class="haze-photo" x="720" y="0" width="480" height="397" fill="url(#hazeTone)" role="img" aria-label="Faded photo of a baby playing on a soft mat"/>

    <polygon class="hero-photo" points="0,0 429,0 232,457 0,457" fill="url(#photoTone)" role="img" aria-label="Smiling baby in a striped outfit lying on a green exercise ball"/>

    <polygon points="413,0 518,0 450,112 368,112" fill="var(--lime)"/>
    <polygon points="30,214 104,214 0,392 0,266" fill="var(--lime)" opacity="0.85"/>
    <polygon points="288,369 380,369 330,457 238,457" fill="var(--lime)"/>
    <polygon points="393,397 1200,397 1200,457 358,457" fill="var(--lime)"/>

    <line x1="308" y1="0" x2="160" y2="240" stroke="var(--navy)" stroke-width="0.8" opacity="0.7"/>
    <line x1="412" y1="340" x2="360" y2="457" stroke="var(--navy)" stroke-width="0.8" opacity="0.6"/>
    <line x1="905" y1="140" x2="860" y2="250" stroke="var(--navy)" stroke-width="0.6" opacity="0.4"/>
  </svg>

  <div class="brand brand--main"><span class="brand-dot"></span>Ember Tumblehall</div>
  <div class="brand brand--small"><span class="brand-dot"></span>Ember Tumblehall</div>

  <p class="kicker">NEW PROGRAM</p>

  <svg class="headline" width="740" height="100" viewBox="0 0 740 100">
    <defs>
      <linearGradient id="headlineFill" x1="0" y1="0" x2="0" y2="1">
        <stop offset="0" stop-color="#0f1c36"/>
        <stop offset="0.55" stop-color="#1d3a2a"/>
        <stop offset="1" stop-color="#4f8a1c"/>
      </linearGradient>
    </defs>
    <text x="8" y="84" textLength="720" lengthAdjust="spacingAndGlyphs"
          font-family="'Black Ops One', sans-serif" font-size="92"
          fill="url(#headlineFill)" stroke="#0f1c36" stroke-width="7"
          stroke-linejoin="round" paint-order="stroke">SENSORY PLAY</text>
    <text x="8" y="84" textLength="720" lengthAdjust="spacingAndGlyphs"
          font-family="'Black Ops One', sans-serif" font-size="92"
          fill="url(#headlineFill)" stroke="#ffffff" stroke-width="1.5"
          paint-order="stroke">SENSORY PLAY</text>
  </svg>

  <div class="audience">FOR BABIES 0 - 13 MONTHS OLD</div>

  <div class="schedule">
    <div class="schedule-day">
      <span class="schedule-label">STARTING ON</span>
      <span class="schedule-weekday">WEDNESDAYS</span>
    </div>
    <span class="schedule-divider"></span>
    <div class="schedule-month">
      <span class="schedule-year">2022</span>
      <span class="schedule-name">FEBRUARY</span>
    </div>
  </div>

  <div class="contact-item contact-item--phone">
    <svg width="32" height="30" viewBox="0 0 32 30">
      <path d="M3 11 Q16 1 29 11 L26 15 L21 13 L21 10 Q16 8 11 10 L11 13 L6 15 Z" fill="var(--navy)"/>
      <rect x="6" y="16" width="20" height="12" rx="2" fill="var(--navy)"/>
      <circle cx="16" cy="22" r="3.5" fill="var(--lime)"/>
    </svg>
    <span>97316258</span>
  </div>
  <div class="contact-item contact-item--mail">
    <svg width="36" height="30" viewBox="0 0 36 30">
      <rect x="3" y="9" width="30" height="19" fill="var(--navy)"/>
      <path d="M3 9 L18 20 L33 9" fill="none" stroke="var(--lime)" stroke-width="2"/>
      <rect x="10" y="2" width="16" height="13" fill="var(--paper)" stroke="var(--navy)" stroke-width="1.5"/>
      <line x1="13" y1="6" x2="23" y2="6" stroke="var(--navy)" stroke-width="1.5"/>
      <line x1="13" y1="10" x2="23" y2="10" stroke="var(--navy)" stroke-width="1.5"/>
    </svg>
    <span>INFO@EMBERTUMBLEHALL.EXAMPLE</span>
  </div>
  <div class="contact-item contact-item--web">
    <svg width="32" height="32" viewBox="0 0 32 32">
      <circle cx="16" cy="16" r="13" fill="none" stroke="var(--navy)" stroke-width="2.5"/>
      <ellipse cx="16" cy="16" rx="6" ry="13" fill="none" stroke="var(--navy)" stroke-width="2"/>
      <line x1="3" y1="16" x2="29" y2="16" stroke="var(--navy)" stroke-width="2"/>
      <line x1="5" y1="9" x2="27" y2="9" stroke="var(--navy)" stroke-width="2"/>
      <line x1="5" y1="23" x2="27" y2="23" stroke="var(--navy)" stroke-width="2"/>
    </svg>
    <span>WWW.EMBERTUMBLEHALL.EXAMPLE</span>
  </div>
</div>
</body>
</html>
```